Root Crate Filtration Label Design

Need a sticker or label design for our Root Crate to fit an 8x6" area.

UPDATE 9/21/2015:
We eliminated some text and would like to see only the following on the label:

Root Crate Contains:

- Terrestrial Soil
- Lake Sediment
- Organic Matter
- Natural Bacteria
- Minerals & Trace Elements

"STAY RIVER CALM"

We would love to see an illustration of graphic of the outline of our Root Crate (Black plastic box) showing the soil on the inside which is brown and a thin layer of foam on top of the soil inside the box. On top of the box a layer of natural gravel and the plant roots shown growing through the gravel into the soil inside of the box.

Watch this video to get an idea of how the Root Crate fits in an aquarium under a layer of gravel: https://www.clipvaultly.com/watch?t=92&v=qrTm4kLx8Wd
Updates

Target Market(s)

Customers in Retail Stores

Industry/Entity Type

Pet

Font styles to use
Sans Serif

Colors
9bcb3c
0393ce
0255a3
33b8a4
cadf82
add136
86cfc7
cfeae6
eaf2ce

Requirements
Must have
• Stay River Calm and most of the Text - Text can be changed slightly or simplified
Nice to have
• I have attached a picture of a "FRESHWATER Fish Scene" we like.
Should not have
• NOT Too busy - Trying to keep it as simple as possible - Natural Earthy Colors - Realistic Drawings. DO NOT ADD Marine Fish or other MARINE life. This is strictly for FRESHWATER FISH.

```html
<!DOCTYPE html>
<html lang="en">
<head>
<meta charset="utf-8">
<title>Root Crate Filtration Label</title>
<link href="https://fonts.googleapis.com/css2?family=Montserrat:wght@600;800&family=Open+Sans:wght@600&display=swap" rel="stylesheet">
<style>
  :root {
    --backdrop: #4a2e1f;
    --navy: #0255a3;
    --blue: #0393ce;
    --teal: #33b8a4;
    --aqua: #86cfc7;
    --mint: #cfeae6;
    --pale: #eaf2ce;
    --white: #ffffff;
  }
  * { margin: 0; padding: 0; box-sizing: border-box; }
  html, body { width: 857px; height: 1200px; overflow: hidden; }
  body {
    background: var(--backdrop);
    position: relative;
    font-family: "Open Sans", Arial, sans-serif;
  }
  .label {
    position: absolute;
    left: 237px;
    width: 386px;
    overflow: hidden;
    background: linear-gradient(180deg, var(--white) 0%, var(--mint) 45%);
    box-shadow: 0 6px 14px rgba(0,0,0,0.45);
  }
  .label--first { top: 371px; height: 386px; }
  .label--second { top: 777px; height: 366px; }

  .brand {
    position: absolute;
    left: 0; right: 0;
    top: 40px;
    text-align: center;
  }
  .brand__name {
    font-family: "Montserrat", Arial, sans-serif;
    font-weight: 800;
    font-size: 54px;
    line-height: 1;
    letter-spacing: 1px;
    color: var(--navy);
  }
  .brand__sub {
    font-family: "Montserrat", Arial, sans-serif;
    font-weight: 600;
    font-size: 25px;
    letter-spacing: 3px;
    color: var(--blue);
    margin-top: 4px;
  }

  .scene {
    position: absolute;
    left: 0; right: 0; bottom: 0;
    top: 43%;
    background: linear-gradient(180deg, var(--teal) 0%, var(--aqua) 45%, var(--mint) 100%);
  }
  .wave {
    position: absolute;
    left: 0;
    top: calc(43% - 24px);
    width: 100%;
    height: 48px;
  }

  .contents {
    position: absolute;
    left: 0; right: 0;
    top: 52%;
    text-align: center;
    color: var(--white);
    font-size: 13.5px;
    line-height: 1.55;
    text-shadow: 0 1px 2px rgba(2,85,163,0.6);
  }
  .contents span { padding: 0 4px; }
  .tagline {
    position: absolute;
    left: 0; right: 0;
    top: 69%;
    text-align: center;
    font-family: "Montserrat", Arial, sans-serif;
    font-weight: 800;
    font-size: 23px;
    letter-spacing: 1px;
    color: var(--white);
    text-shadow: 0 1px 3px rgba(2,85,163,0.6);
  }
</style>
</head>
<body>

  <section class="label label--first">
    <div class="scene" role="img" aria-label="Freshwater underwater scene with plants, bubbles and small fish"></div>
    <svg class="wave" viewBox="0 0 386 48" preserveAspectRatio="none" aria-hidden="true">
      <path d="M0 30 C80 8 150 8 210 24 C270 40 330 40 386 18 L386 48 L0 48 Z" fill="var(--teal)"/>
      <path d="M0 30 C80 8 150 8 210 24 C270 40 330 40 386 18" fill="none" stroke="var(--navy)" stroke-width="3"/>
    </svg>
    <div class="brand">
      <div class="brand__name">Root Crate</div>
      <div class="brand__sub">FILTRATION</div>
    </div>
    <div class="contents">
      <div>Terrestrial Soil <span>|</span> Lake Sediment <span>|</span> Organic Matter</div>
      <div>Natural Bacteria <span>|</span> Minerals <span>|</span> Trace Elements</div>
    </div>
    <div class="tagline">STAY RIVER CALM</div>
  </section>

  <section class="label label--second">
    <div class="scene" role="img" aria-label="Freshwater underwater scene with plants, bubbles and small fish"></div>
    <svg class="wave" viewBox="0 0 386 48" preserveAspectRatio="none" aria-hidden="true">
      <path d="M0 20 C70 40 140 40 200 24 C260 8 320 6 386 26 L386 48 L0 48 Z" fill="var(--teal)"/>
      <path d="M0 20 C70 40 140 40 200 24 C260 8 320 6 386 26" fill="none" stroke="var(--navy)" stroke-width="3"/>
    </svg>
    <div class="brand">
      <div class="brand__name">Root Crate</div>
      <div class="brand__sub">FILTRATION</div>
    </div>
    <div class="contents">
      <div>Terrestrial Soil <span>|</span> Lake Sediment <span>|</span> Organic Matter</div>
      <div>Natural Bacteria <span>|</span> Minerals <span>|</span> Trace Elements</div>
    </div>
    <div class="tagline">STAY RIVER CALM</div>
  </section>

</body>
</html>
```